Design logo, business cards and letterhead for my eye surgery (doctor's) practice

I am a young eye surgeon (Ophthalmic Surgeon) and I need business cards and letterhead designed ( I have a business card brief and a stationary brief submitted). A small logo would also be useful, or some shape that is seen on both the cards and the letterhead. I am based in Perth, Western Australia. I do some laser refractive work ie LASIK, but also other aspects of ophthalmology as well. The design should be conservative, professional and classic, but also, (as someone who sees young patients for laser surgery) a little interesting to people who refer to me and to patients who will be given my card. The details on the letterhead should be:
Dr Ned Palliser
MBBS (Hons), MMed, FRANZCO
Ophthalmic Surgeon

27 Waverton Ave, Subiaco
Western Australia 6008
Phone: (08) 9217 4602
Facsimile: (08) 9217 4619
Email: reception@nedpalliser.com.au
Provider No: 618095KW

The information on the cards should be the same, but with out the provider number.
On the back of the card should say-

Next Appointment________
The rooms can be accessed easily via public transport, or please feel free to park behind the premises in the designated parking bays.

Target Market(s)

General practitioners and optometrists who refer to me and patients

Industry/Entity Type

Business

Contact Information for Business Card

See above

Requirements
Nice to have
• I've attached a little photo which I thought may make a cute logo of sorts on the cards and letterhead.

```html
<!DOCTYPE html>
<html lang="en">
<head>
<meta charset="utf-8">
<title>Dr Ned Palliser – Business Cards</title>
<link rel="stylesheet" href="https://fonts.googleapis.com/css2?family=Tinos:wght@400;700&family=Open+Sans:wght@400&family=Nunito:wght@800&display=swap">
<style>
  :root {
    --page: #ffffff;
    --name-red: #e8302a;
    --quals-blue: #2234c8;
    --specialty-green: #4fdc1a;
    --ink: #111111;
    --logo-blue: #1f3fd0;
    --band-blue: #3cb6e6;
    --band-red: #f2392a;
    --cyan-wash: #d3f0f8;
    --pink-wash: #f8c3d6;
  }
  * { box-sizing: border-box; margin: 0; padding: 0; }
  html, body { width: 1200px; height: 893px; overflow: hidden; background: var(--page); }
  .sheet { position: relative; width: 1200px; height: 893px; }

  .card {
    position: absolute;
    width: 537px;
    height: 356px;
    overflow: hidden;
    font-family: "Tinos", "Times New Roman", serif;
    color: var(--ink);
  }
  .card--blue { background: linear-gradient(160deg, #ffffff 0%, #f4fbfd 35%, var(--cyan-wash) 70%, #eaf8fc 100%); }
  .card--pink { background: linear-gradient(160deg, #ffffff 0%, #fdeef3 30%, var(--pink-wash) 70%, #f6b0c8 100%); }

  .card--front.row-1 { left: 53px; top: 42px; }
  .card--back.row-1  { left: 607px; top: 42px; }
  .card--front.row-2 { left: 53px; top: 482px; }
  .card--back.row-2  { left: 607px; top: 482px; }

  .band { position: absolute; left: 0; right: 0; bottom: 0; height: 55px; }
  .card--blue .band { background: var(--band-blue); }
  .card--pink .band { background: var(--band-red); }

  .brand {
    position: absolute;
    display: flex;
    align-items: center;
    gap: 8px;
    font-family: "Tinos", "Times New Roman", serif;
    font-weight: 700;
    font-size: 19px;
    color: var(--logo-blue);
    white-space: nowrap;
  }
  .brand__dot { width: 30px; height: 30px; border-radius: 50%; background: var(--logo-blue); }
  .card--front .brand { left: 14px; top: 42px; }
  .card--back .brand { left: 50%; transform: translateX(-50%); top: 50px; }
  .row-2.card--back .brand { top: 56px; }

  .name {
    position: absolute; left: 172px; top: 35px;
    font-weight: 700; font-size: 37px; color: var(--name-red); white-space: nowrap; letter-spacing: 0.2px;
  }
  .quals {
    position: absolute; right: 14px; top: 79px;
    font-size: 18px; color: var(--quals-blue); white-space: nowrap;
  }
  .specialty {
    position: absolute; right: 16px; top: 106px;
    font-family: "Nunito", Arial, sans-serif; font-weight: 800; font-size: 22px;
    color: var(--specialty-green); white-space: nowrap;
  }
  .contact { position: absolute; left: 0; right: 0; top: 186px; text-align: center; }
  .contact__address { font-size: 20.5px; line-height: 32px; }
  .contact__line { font-size: 24px; line-height: 34px; }
  .email {
    position: absolute; left: 20px; bottom: 0; height: 55px; line-height: 55px;
    font-family: "Open Sans", Arial, sans-serif; font-size: 25px; color: #ffffff; white-space: nowrap;
  }

  .notes {
    position: absolute; left: 25px; right: 14px; top: 144px;
    font-size: 24px; line-height: 33px;
  }
  .row-2 .notes { top: 156px; }
</style>
</head>
<body>
<main class="sheet">

  <section class="card card--front card--blue row-1">
    <div class="brand"><span class="brand__dot"></span>Palliser Eye</div>
    <h1 class="name">Dr. Ned Palliser</h1>
    <p class="quals">MBBS (Hons), MMed, FRANZCO</p>
    <p class="specialty">Ophthalmic Surgeon</p>
    <div class="contact">
      <p class="contact__address">27 Waverton Ave, Subiaco, Western Australia 6008</p>
      <p class="contact__line">Phone: (08) 9217 4602</p>
      <p class="contact__line">Facsimile: (08) 9217 4619</p>
    </div>
    <div class="band"></div>
    <p class="email">Email: reception@nedpalliser.com.au</p>
  </section>

  <section class="card card--back card--blue row-1">
    <div class="brand"><span class="brand__dot"></span>Palliser Eye</div>
    <p class="notes">Next Appointment________<br>The rooms can be accessed easily via public transport, or please feel free to park behind the premises in the designated parking bays.</p>
    <div class="band"></div>
  </section>

  <section class="card card--front card--pink row-2">
    <div class="brand"><span class="brand__dot"></span>Palliser Eye</div>
    <h1 class="name">Dr. Ned Palliser</h1>
    <p class="quals">MBBS (Hons), MMed, FRANZCO</p>
    <p class="specialty">Ophthalmic Surgeon</p>
    <div class="contact">
      <p class="contact__address">27 Waverton Ave, Subiaco, Western Australia 6008</p>
      <p class="contact__line">Phone: (08) 9217 4602</p>
      <p class="contact__line">Facsimile: (08) 9217 4619</p>
    </div>
    <div class="band"></div>
    <p class="email">Email: reception@nedpalliser.com.au</p>
  </section>

  <section class="card card--back card--pink row-2">
    <div class="brand"><span class="brand__dot"></span>Palliser Eye</div>
    <p class="notes">Next Appointment________<br>The rooms can be accessed easily via public transport, or please feel free to park behind the premises in the designated parking bays.</p>
    <div class="band"></div>
  </section>

</main>
</body>
</html>
```